Physician House Call Doctor

I need 2 newspaper color display adds. 1 small and 1 larger. I have attached some ideas but they need to be updated, more professional and eye-catching . I may also want to change the doctors picture and add some text. I need submit to newspaper in a PDF format and the adds must have a border.

```html
<!DOCTYPE html>
<html lang="en">
<head>
<meta charset="utf-8">
<title>Physician House Calls – Newspaper Display Ads</title>
<link href="https://fonts.googleapis.com/css2?family=Anton&family=Ubuntu:wght@300;400;500;700&family=Roboto:wght@400;700&display=swap" rel="stylesheet">
<style>
  :root{
    --board:#383838;
    --navy:#2b2a6b;
    --green:#16943f;
    --black:#0b0b0b;
    --white:#ffffff;
    --mist:#ececec;
    --photo-a:#5b6f7d;
    --photo-b:#c79a86;
    --heart-a:#f1e6e2;
    --heart-b:#d8323a;
    --caption:#f2f2f2;
    --ink:#1b1b1b;
  }
  *{box-sizing:border-box;margin:0;padding:0}
  html,body{width:1200px;height:1200px;overflow:hidden;background:var(--board)}
  .board{position:relative;width:1200px;height:1200px}

  .ad{position:absolute;overflow:hidden;box-shadow:0 4px 14px rgba(0,0,0,.45)}
  .abs{position:absolute;white-space:nowrap}

  /* ---------- small ad ---------- */
  .ad-small{left:102px;top:247px;width:456px;height:659px;
    background:linear-gradient(180deg,var(--mist) 0%,#f6f6f6 60%);font-family:"Ubuntu",sans-serif}
  .ad-small .navy-field{left:0;top:362px;width:456px;height:248px;background:var(--navy)}
  .ad-small .url-band{left:0;top:610px;width:456px;height:49px;background:var(--green);
    color:var(--white);font-weight:700;font-size:23px;text-align:center;line-height:48px;letter-spacing:.3px}
  .ad-small .portrait-ring{left:32px;top:21px;width:392px;height:392px;border-radius:50%;background:var(--white)}
  .ad-small .portrait{left:39px;top:28px;width:378px;height:378px;border-radius:50%;
    background:radial-gradient(circle at 50% 45%,var(--photo-b) 0%,#9a8a86 35%,var(--photo-a) 70%)}
  .ad-small .badge{left:8px;top:258px;width:124px;height:124px;border-radius:50%;background:var(--navy);
    border:3px solid var(--green);color:var(--white);font-weight:500;font-size:18.5px;line-height:23.5px;
    display:flex;align-items:center;justify-content:center;text-align:center}
  .ad-small .heart{left:107px;top:355px;width:80px;height:80px;border-radius:50%;border:3px solid var(--white);
    background:radial-gradient(circle at 50% 45%,var(--heart-b) 0%,#e57a7a 35%,var(--heart-a) 70%)}
  .ad-small .phone-band{left:274px;top:330px;width:182px;height:37px;background:var(--black);
    color:var(--white);font-family:"Anton",sans-serif;font-size:26px;line-height:37px;padding-left:18px;letter-spacing:.3px}
  .ad-small .phone-icon{left:190px;top:302px;width:88px;height:88px}
  .ad-small .headline{left:13px;top:443px;color:var(--white);font-family:"Anton",sans-serif;font-size:33px;line-height:35px;letter-spacing:.3px}
  .ad-small .rule{left:13px;top:521px;width:225px;height:1px;background:#8a89b5}
  .ad-small .doctor{left:16px;top:533px;color:var(--white);font-size:20.5px;line-height:27px}
  .ad-small .doctor strong{font-weight:500}
  .ad-small .divider{left:250px;top:433px;width:1px;height:163px;background:#9c9bc4}
  .ad-small .notes{left:260px;top:433px;color:var(--white);font-weight:300;font-size:19px;line-height:24px}
  .ad-small .notes p{margin-bottom:9px}

  /* ---------- large ad ---------- */
  .ad-large{left:601px;top:396px;width:522px;height:515px;background:var(--white);font-family:"Ubuntu",sans-serif;color:var(--ink)}
  .ad-large .title{left:12px;top:22px;color:var(--green);font-family:"Anton",sans-serif;font-size:27px;line-height:32px;letter-spacing:.3px}
  .ad-large .subtitle{left:12px;top:55px;color:var(--navy);font-family:"Roboto",sans-serif;font-size:24px;line-height:28px}
  .ad-large .intro{left:0;top:88px;width:522px;height:80px;background:var(--navy);color:var(--white);
    font-size:15px;line-height:18.4px;padding:3px 0 0 13px}
  .ad-large .portrait{left:273px;top:30px;width:246px;height:246px;border-radius:50%;
    background:radial-gradient(circle at 55% 50%,var(--photo-b) 0%,#8e8a90 35%,#2f4a63 72%)}
  .ad-large .body{left:15px;font-size:13.8px;line-height:18.4px}
  .ad-large .hours{left:167px;top:204px;width:184px;height:184px;border-radius:50%;background:var(--green);
    color:var(--white);text-align:center;font-family:"Anton",sans-serif;padding-top:36px;white-space:nowrap}
  .ad-large .hours .lead{font-size:19px;line-height:22px;letter-spacing:.4px}
  .ad-large .hours .small{font-family:"Roboto",sans-serif;font-weight:700;font-size:14px;line-height:18px;margin-top:4px}
  .ad-large .credentials{left:349px;top:252px;width:152px;height:152px;border-radius:50%;background:var(--navy);
    color:var(--white);text-align:center;padding-top:48px;font-size:12.5px;line-height:15.5px;white-space:nowrap}
  .ad-large .credentials strong{display:block;font-size:16px;font-weight:700;line-height:20px}
  .ad-large .heart{left:300px;top:351px;width:70px;height:70px;border-radius:50%;border:2px solid var(--ink);
    background:radial-gradient(circle at 50% 50%,var(--heart-b) 0%,#e88a8a 30%,var(--heart-a) 65%)}
  .ad-large .notice{left:14px;top:431px;font-size:13px;font-weight:700;line-height:16px}
  .ad-large .contact-band{left:0;top:453px;width:522px;height:25px;background:var(--green);color:var(--white);
    font-size:14.5px;line-height:25px;padding-left:13px}
  .ad-large .contact-band strong{font-weight:700}
  .ad-large .footer{left:0;top:478px;width:522px;height:37px;background:var(--navy);color:var(--white);
    font-size:12.5px;line-height:28px;text-align:center}
  .ad-large .footer .line{position:absolute;top:14px;height:1px;background:var(--white)}

  .caption{position:absolute;color:var(--caption);font-family:"Ubuntu",sans-serif;font-weight:300;font-size:24px;text-align:center}
</style>
</head>
<body>
<main class="board">

  <section class="ad ad-small" aria-label="Small ad">
    <div class="abs navy-field"></div>
    <div class="abs portrait-ring"></div>
    <div class="abs portrait" role="img" aria-label="Portrait photo of the physician in a white coat with stethoscope"></div>
    <div class="abs badge">Board<br>Certified<br>Family<br>Practice</div>
    <div class="abs heart" role="img" aria-label="Photo of hands holding a red heart"></div>
    <div class="abs phone-band">202-555-0147</div>
    <svg class="abs phone-icon" viewBox="0 0 88 88" aria-hidden="true">
      <circle cx="44" cy="44" r="43" fill="none" stroke="#fff" stroke-width="1.5"/>
      <circle cx="44" cy="44" r="37" fill="#16943f" stroke="#fff" stroke-width="2"/>
      <circle cx="44" cy="44" r="25" fill="none" stroke="#fff" stroke-width="3"/>
      <path d="M35 31c2-1 3 0 4 2l2 4c1 2 0 3-1 4l-1 1c1 3 4 6 7 7l1-1c1-1 2-2 4-1l4 2c2 1 3 2 2 4l-1 2c-2 3-6 3-10 1-6-3-11-8-14-14-2-4-2-8 1-10z" fill="#fff"/>
    </svg>
    <h1 class="abs headline">PHYSICIAN HOUSE<br>Calls are back !</h1>
    <div class="abs rule"></div>
    <p class="abs doctor"><strong>Dr. Martin R Hale</strong><br>comes to your home!</p>
    <div class="abs divider"></div>
    <div class="abs notes">
      <p>Flu Shots now<br>available</p>
      <p>Why go out in the<br>rain or snow?</p>
      <p>Medicare accepted<br>for qualified patients</p>
    </div>
    <div class="abs url-band">www.capitolhomemd.com</div>
  </section>

  <section class="ad ad-large" aria-label="Larger ad">
    <div class="abs intro"><p>Can’t get to the doctor or your doctor<br>can’t see you right away, <strong>Dr.Hale</strong><br>will come to you. He is Glen Haven<br>and the surrounding area!</p></div>
    <h2 class="abs title">PHYSICIAN HOUSE CALLS</h2>
    <p class="abs subtitle">Affordable &amp; Convenient</p>
    <div class="abs portrait" role="img" aria-label="Portrait photo of the physician in a white coat with stethoscope"></div>
    <p class="abs body" style="top:177px">Medicare is accepted for<br>qualified patients,you<br>pay a small trip fee<br>for your house call.</p>
    <p class="abs body" style="top:259px">Dr.Hale does<br>family consults,<br>second opinions<br>medical testing and<br>evaluations.</p>
    <p class="abs body" style="top:361px">We also offer Lab Testing,<br>X-rays Breathing Treatments<br>all in the comfort of your home.</p>
    <div class="abs hours">
      <div class="lead">CONVENIENT<br>DAYTIME HOURS<br>&amp;</div>
      <div class="small">Open most evenings,<br>weekends,and holidays!</div>
    </div>
    <div class="abs credentials"><strong>Martin R. Hale</strong>MD Primary &amp; Urgent Care<br>Board Certified<br>Family Medicine</div>
    <div class="abs heart" role="img" aria-label="Photo of hands holding a red heart"></div>
    <p class="abs notice">Medicinal Marijuana recommendation is now available in Maryland.</p>
    <div class="abs contact-band">Call : <strong>202-555-0147</strong> or Visit : <strong>www.capitolhomemd.com</strong> for more information.</div>
    <div class="abs footer">
      <span class="line" style="left:0;width:92px"></span>
      Keep this advertisement handy for future reference.
      <span class="line" style="left:415px;width:107px"></span>
    </div>
  </section>

  <p class="caption" style="left:132px;top:938px;width:400px">Small ad 2.25W x 3.25H.</p>
  <p class="caption" style="left:648px;top:930px;width:400px">Larger ad4.6875W x 4.625h</p>

</main>
</body>
</html>
```